Business card for Full Stable Works Vanhoorne

I would like to have me designed an professional business card with my existing logo for my company called : full stable works vanhoorne gcv.
I prefer a two sided business card with on the back side only the horses head and the website : fswvanhoorne-example.eu
Only one colour shouldbe all right.
The logo must appear in a nic professional way on the business card.

Other suggestion are welcome.

All copy wrights must be released by the designer after we have selected a final design.

Target Market(s)

Equestrian businesses

Industry/Entity Type

Business

Contact Information for Business Card

Gerard Vanhoorne
Title: zaakvoerder
Full Stable Works Vanhoorne GCV
Lindekouter 47
B - 9999 Voorbeeldegem
België
Phone: + 32 400 98 76 10
Mail: gerard@fswvanhoorne-example.eu

Font styles to use
Serif

Requirements
Must have
• My own logo
• See attached files
• Website: fswvanhoorne-example.eu

```html
<!DOCTYPE html>
<html lang="nl">
<head>
<meta charset="utf-8">
<title>Full Stable Works Vanhoorne – Business Card</title>
<link rel="stylesheet" href="https://fonts.googleapis.com/css2?family=Bebas+Neue&family=Encode+Sans+Condensed:wght@300;500&family=Ubuntu:wght@400;500;700&display=swap">
<style>
  :root {
    --page: #ffffff;
    --card-dark: #232323;
    --card-dark-light: #2e2e2e;
    --card-light: #f4f4f4;
    --ink: #2a3242;
    --green: #7dc242;
    --green-soft: #d9ebc6;
    --ribbon: #2c2c2c;
    --ribbon-edge: #3a3a3a;
  }
  * { margin: 0; padding: 0; box-sizing: border-box; }
  html, body {
    width: 848px; height: 1200px; overflow: hidden;
    background: var(--page);
  }
  .sheet { position: relative; width: 848px; height: 1200px; }

  /* Back side */
  .card-back {
    position: absolute; left: 125px; top: 89px; width: 280px; height: 467px;
    background:
      linear-gradient(60deg, transparent 49.5%, rgba(255,255,255,0.03) 50%) ,
      linear-gradient(-60deg, transparent 49.5%, rgba(255,255,255,0.03) 50%),
      var(--card-dark);
    overflow: hidden;
  }
  .back-emblem {
    position: absolute; left: 53px; top: 113px; width: 177px; height: 218px;
    border-radius: 50% 40% 45% 50%;
    background: linear-gradient(160deg, #8ccd52, var(--green));
  }
  .back-ribbon {
    position: absolute; left: 34px; top: 254px; width: 217px; height: 30px;
    background: var(--ribbon);
    border: 1px solid var(--ribbon-edge);
    display: flex; align-items: center; justify-content: center;
  }
  .back-ribbon::before, .back-ribbon::after {
    content: ""; position: absolute; top: 4px; width: 26px; height: 22px;
    background: var(--ribbon-edge);
  }
  .back-ribbon::before { left: -22px; clip-path: polygon(0 0,100% 0,100% 100%,0 100%,8px 50%); }
  .back-ribbon::after { right: -22px; clip-path: polygon(0 0,100% 0,calc(100% - 8px) 50%,100% 100%,0 100%); }
  .back-url {
    position: relative; z-index: 1;
    font-family: "Bebas Neue", sans-serif; font-size: 17px; letter-spacing: 0.3px;
    color: #e8e8e8;
  }
  .back-url strong { color: #ffffff; font-weight: 400; }

  /* Front side */
  .card-front {
    position: absolute; left: 453px; top: 89px; width: 278px; height: 464px;
    background: var(--card-light);
    overflow: hidden;
    color: var(--ink);
    text-align: center;
  }
  .front-emblem {
    position: absolute; left: 15px; top: 69px; width: 251px; height: 294px;
    border-radius: 50% 45% 40% 50%;
    background: radial-gradient(circle at 55% 40%, var(--green-soft), rgba(217,235,198,0.35));
  }
  .front-brand {
    position: absolute; left: 0; right: 0; top: 42px;
    display: flex; align-items: center; justify-content: center; gap: 7px;
    font-family: "Ubuntu", sans-serif; font-weight: 700; font-size: 15px;
    color: var(--ink);
  }
  .front-brand .dot { width: 14px; height: 14px; border-radius: 50%; background: var(--ink); }
  .front-name {
    position: absolute; left: 0; right: 0; top: 112px;
    font-family: "Ubuntu", sans-serif; font-size: 26px; line-height: 31px;
    letter-spacing: 0.5px;
  }
  .front-name .first { font-weight: 500; display: block; }
  .front-name .last { font-weight: 400; display: block; }
  .front-details {
    position: absolute; left: 0; right: 0; top: 212px;
    font-family: "Encode Sans Condensed", sans-serif; font-weight: 300;
    font-size: 16px; line-height: 22.2px;
  }
  .front-details .title-value { font-weight: 500; }
  .rule {
    position: absolute; left: 41px; width: 192px; height: 1.5px; background: var(--ink);
  }
  .rule-top { top: 352px; }
  .rule-bottom { top: 395px; }
  .front-phone {
    position: absolute; left: 0; right: 0; top: 359px;
    font-family: "Ubuntu", sans-serif; font-weight: 700; font-size: 23px;
  }
  .front-contact {
    position: absolute; left: 0; right: 0; top: 401px;
    font-family: "Ubuntu", sans-serif; font-weight: 700; font-size: 13px; line-height: 16px;
  }
</style>
</head>
<body>
<main class="sheet">
  <section class="card-back" aria-label="Back side">
    <div class="back-emblem" role="img" aria-label="Green horse head emblem"></div>
    <div class="back-ribbon">
      <span class="back-url">www.<strong>FSWVANHOORNE-EXAMPLE</strong>.eu</span>
    </div>
  </section>

  <section class="card-front" aria-label="Front side">
    <div class="front-emblem" role="img" aria-label="Faint horse head emblem in the background"></div>
    <div class="front-brand"><span class="dot"></span>Full Stable Works Vanhoorne</div>
    <h1 class="front-name"><span class="first">GERARD</span><span class="last">VANHOORNE</span></h1>
    <p class="front-details">
      Title: <span class="title-value">zaakvoerder</span><br>
      Full Stable Works<br>
      Vanhoorne GCV<br>
      Lindekouter 47<br>
      B - 9999 Voorbeeldegem<br>
      België
    </p>
    <div class="rule rule-top"></div>
    <p class="front-phone">+ 32 400 98 76 10</p>
    <div class="rule rule-bottom"></div>
    <p class="front-contact">
      gerard@fswvanhoorne-example.eu<br>
      fswvanhoorne-example.eu
    </p>
  </section>
</main>
</body>
</html>
```